Yonder Book Cover for a new author entering the writing space

Design a stunning, eye catching book cover for a Christian Book. Front, back & spine needs to be designed. I am currently reviewing the final draft so the cover will need to be finalized for print once I have the number of pages and the back cover information.

Book Title: Yonder
Book Subtitle: Walking the path ahead with faith.

Author Name: Dr. Calvin Maddox

Target Market(s)

Christian readers

Industry/Entity Type

Christian

Colors

Designer to choose colors to be used in the design.

Requirements
Must have
• Bold Title
• Bold Author
• Bold color
• Clean design
Should not have
• No angel wings
• No hands coming out of heaven
• No doves

```html
<!DOCTYPE html>
<html lang="en">
<head>
<meta charset="UTF-8">
<title>Yonder — Book Cover</title>
<link href="https://fonts.googleapis.com/css2?family=Oswald:wght@400;500&display=swap" rel="stylesheet">
<style>
  :root {
    --page-bg: #ffffff;
    --sky-top: #4b66a2;
    --sky-mid: #8fa4c6;
    --sky-pale: #cdd6dc;
    --horizon-gold: #f2c46e;
    --land-dark: #1c1d22;
    --water-light: #9aa4a8;
    --water-deep: #2b3148;
    --spine-blue: #3f5b9a;
    --spine-edge: #2f4782;
    --type-white: #ffffff;
  }
  * { margin: 0; padding: 0; box-sizing: border-box; }
  html, body {
    width: 1200px;
    height: 1200px;
    overflow: hidden;
    background: var(--page-bg);
  }
  .canvas {
    position: relative;
    width: 1200px;
    height: 1200px;
    font-family: "Oswald", "Arial Narrow", sans-serif;
    color: var(--type-white);
  }
  .front-cover {
    position: absolute;
    left: 214px;
    top: 224px;
    width: 543px;
    height: 754px;
    overflow: hidden;
  }
  .cover-scene {
    position: absolute;
    inset: 0;
    background: linear-gradient(
      to bottom,
      var(--sky-top) 0%,
      #6a84b6 22%,
      var(--sky-mid) 38%,
      var(--sky-pale) 50%,
      #e8dcb4 56%,
      var(--horizon-gold) 59%,
      var(--land-dark) 60.5%,
      var(--land-dark) 66%,
      #c7c08e 67.5%,
      var(--water-light) 73%,
      #5b6680 84%,
      var(--water-deep) 100%
    );
  }
  .cover-title {
    position: absolute;
    top: 62px;
    left: 0;
    width: 100%;
    text-align: center;
    font-weight: 500;
    font-size: 122px;
    line-height: 1;
    letter-spacing: 0.14em;
    padding-left: 0.14em;
  }
  .cover-subtitle {
    position: absolute;
    top: 224px;
    left: 0;
    width: 100%;
    text-align: center;
    font-weight: 400;
    font-size: 22px;
    line-height: 36px;
    letter-spacing: 0.08em;
    text-transform: uppercase;
  }
  .cover-author {
    position: absolute;
    top: 652px;
    left: 0;
    width: 100%;
    text-align: center;
    font-weight: 400;
    font-size: 38px;
    letter-spacing: 0.14em;
    padding-left: 0.14em;
    text-transform: uppercase;
  }
  .spine {
    position: absolute;
    left: 870px;
    top: 218px;
    width: 96px;
    height: 764px;
    background: linear-gradient(to right, #6a82b8 0%, var(--spine-blue) 14%, var(--spine-blue) 82%, var(--spine-edge) 100%);
  }
  .spine-text {
    position: absolute;
    left: 0;
    width: 100%;
    display: flex;
    justify-content: center;
    writing-mode: vertical-rl;
    white-space: nowrap;
    text-transform: uppercase;
    line-height: 1;
  }
  .spine-title {
    top: 72px;
    font-weight: 500;
    font-size: 64px;
    letter-spacing: 0.04em;
  }
  .spine-author {
    top: 464px;
    font-weight: 400;
    font-size: 28px;
    letter-spacing: 0.06em;
  }
</style>
</head>
<body>
  <main class="canvas">
    <section class="front-cover">
      <div class="cover-scene" role="img" aria-label="Sunset photograph: a silhouetted figure standing on a dark rocky shore, reflected in still water under a blue-to-gold sky"></div>
      <h1 class="cover-title">YONDER</h1>
      <p class="cover-subtitle">Walking the path ahead<br>with faith</p>
      <p class="cover-author">Dr. Calvin Maddox</p>
    </section>
    <aside class="spine">
      <span class="spine-text spine-title">Yonder</span>
      <span class="spine-text spine-author">Dr. Calvin Maddox</span>
    </aside>
  </main>
</body>
</html>
```